10-slide template for ESG report for small businesses in Europe

Presentation goal: for owners of small businesses in Europe to report on their ESG metrics to various internal and external stakeholders, but typically used as part of their annual (financial) report.
Who is the target audience: small business owners/managers in Europe (these are business people, but not very corporate)
How is it going to be used: this template will be used to generate PDF reports automatically based on various inputs. The final output will not be reviewed or corrected by a human; hence we need to make sure that the template is flexible enough to be used for a variety of different inputs (specifically, in some cases there will be no input, and in some cases there will be many characters).
Desired look and feel: following VelloCrest brand style guide (attached). It's for business use so it's somewhat formal, but I do not want it to come across too corporate, so it's OK if there are playful elements.
What is the catch: the fact the template will need to be flexible enough to allow for the report to still look OK even if a certain fields do not have a value (specifically, as mentioned earlier there are some text fields that are likely going to be empty, but could have up to 1000 characters of text).
Illustrations: to keep it generic and relevant for a variety of businesses across all of Europe it's probably better to use simple flat style illustrations instead of photos. I've been using https://brimstudiofy.com/ to create those (see example attached) but I'm open to anything.
Lastly: please note that I'm very open to changing the position and size of all copy, tables, illustrations etc. I know I'm a terrible designer - that's why I'm here ;-)
Look and feel
Each slider illustrates characteristics of the customer's brand and the style your logo design should communicate.

```html
<!DOCTYPE html>
<html lang="en">
<head>
<meta charset="utf-8">
<title>People – ESG Report</title>
<link href="https://fonts.googleapis.com/css2?family=Arimo:wght@400;700&display=swap" rel="stylesheet">
<style>
  :root {
    --brand-green: #99cc00;
    --title-green: #8fd14f;
    --panel-green: #cfe583;
    --field-blue: #3b7ddd;
    --ink: #111111;
    --muted: #9a9a9a;
    --rule: #a6a6a6;
    --paper: #ffffff;
  }
  * { box-sizing: border-box; margin: 0; padding: 0; }
  html, body { width: 1200px; height: 672px; overflow: hidden; background: var(--paper); }
  body { font-family: "Arimo", Arial, sans-serif; color: var(--ink); }

  .slide { position: relative; width: 1200px; height: 672px; overflow: hidden; background: var(--paper); }

  .side-band { position: absolute; left: 992px; top: 0; width: 208px; height: 672px; background: var(--brand-green); }
  .band-illustration {
    position: absolute; left: 1020px; top: 56px; width: 176px; height: 196px;
    background: radial-gradient(circle at 50% 50%, #b8dd4d 0%, var(--brand-green) 72%);
    border-radius: 12px;
  }

  .client-logo { position: absolute; left: 134px; top: 62px; font-size: 23px; font-weight: 700; color: var(--field-blue); }

  .section-title {
    position: absolute; right: 304px; top: 96px;
    font-size: 48px; font-weight: 400; color: var(--title-green); line-height: 1;
  }
  .title-rule { position: absolute; left: 137px; top: 154px; width: 855px; height: 2px; background: var(--brand-green); }

  .intro {
    position: absolute; left: 137px; top: 166px; width: 780px;
    font-size: 12.3px; line-height: 15.4px;
  }

  .metrics-heading { position: absolute; left: 139px; top: 299px; font-size: 19.5px; color: var(--title-green); font-weight: 400; }

  .metrics-table {
    position: absolute; left: 129px; top: 337px; width: 407px;
    border-collapse: collapse; font-size: 11px;
  }
  .metrics-table td { border: 1px solid var(--rule); padding: 0 10px; vertical-align: middle; line-height: 13px; }
  .metrics-table .metric-label { width: 322px; }
  .metrics-table .metric-value { color: var(--field-blue); font-weight: 700; font-size: 11.5px; vertical-align: top; padding-top: 12px; }
  .metrics-table tr:nth-child(1) td { height: 53px; }
  .metrics-table tr:nth-child(2) td { height: 38px; }
  .metrics-table tr:nth-child(3) td { height: 38px; }
  .metrics-table tr:nth-child(4) td { height: 54px; }
  .metrics-table tr:nth-child(5) td { height: 37px; }
  .metrics-table tr:nth-child(6) td { height: 52px; }
  .metrics-table tr:nth-child(5) .metric-value { padding-top: 12px; }

  .commentary-panel {
    position: absolute; left: 612px; top: 332px; width: 329px; height: 277px;
    background: var(--panel-green); border-radius: 11px;
    display: flex; align-items: center; justify-content: center; text-align: center;
    padding: 0 40px;
    color: var(--field-blue); font-weight: 700; font-size: 12px; line-height: 15px;
  }

  .footer { position: absolute; left: 171px; top: 638px; font-size: 12px; color: var(--muted); }
  .footer .field { color: var(--field-blue); }
</style>
</head>
<body>
<main class="slide">
  <div class="side-band"></div>
  <div class="band-illustration" role="img" aria-label="Flat white illustration of four people connected by dashed lines, representing a network of employees"></div>

  <div class="client-logo">[client logo]</div>

  <h1 class="section-title">People</h1>
  <div class="title-rule"></div>

  <p class="intro">Our employees are central to our identity and success as a business. This section outlines our commitment to foster a diverse, equitable workplace where all people feel valued, safe and empowered to reach their full potential. We report on demographics, inclusion initiatives, health and safety, training, and development programs. By tracking this data, we can cultivate talent, prevent risks, uphold ethical labor practices, and ensure our workforce thrives in an environment of belonging, care and purpose.</p>

  <h2 class="metrics-heading">Key metrics</h2>
  <table class="metrics-table">
    <tr><td class="metric-label">% women and minorities on board and management team</td><td class="metric-value">[input]</td></tr>
    <tr><td class="metric-label">Gender pay gap ratio (men:women)</td><td class="metric-value">[input]</td></tr>
    <tr><td class="metric-label">Entry level wage to local living wage ratio</td><td class="metric-value">[input]</td></tr>
    <tr><td class="metric-label">Average number of training hours per employee</td><td class="metric-value">[input]</td></tr>
    <tr><td class="metric-label">Work-related fatalities / injuries at company sites</td><td class="metric-value">[input]</td></tr>
    <tr><td class="metric-label">% employees covered by collective bargaining agreement</td><td class="metric-value">[input]</td></tr>
  </table>

  <div class="commentary-panel">[Paragraph of text between 0 and 1000 characters]</div>

  <p class="footer"><span class="field">[reporting period]</span> Environmental, Social, and Governance Report | <span class="field">[business name]</span></p>
</main>
</body>
</html>
```